Bricks in the Wall

We need graphics for a 5x7 or 6x9 post card, single sided for a small speech language pathology practice that serves pediatric patients primarily with children on the autism spectrum.

I want a brick wall, with words and phrases written into the bricks. (to follow)
A child standing on top of the wall with hands up in success.
A few incomplete autism puzzles on the ground.
A larger complete autism puzzle in the the child's hand.
The title is: Speech/Language Therapy
The Foundation for Communication Success
Words/phrases to go into the red bricks:
Receptive Language, Expressive Language, Pragmatics, Sensory, cognitive,
social language, autism, articulation, TeleTherapy, auditory processing, screening, evaluation, developmental delay, Goals, family involvement, environmental communication, ASD, Mirror Neurons.

Target Market(s)

Children with speech and language disorders.

Industry/Entity Type

Speech and Language Therapy

Font styles to use
Serif

Requirements
Must have
• Colors, primary and red bricks.
Nice to have
• I want the postcard to have a happy feel to it and a sense of success.
Should not have
• I don't want it cluttered.

```html
<!DOCTYPE html>
<html lang="en">
<head>
<meta charset="utf-8">
<title>Speech/Language Therapy Postcard</title>
<link href="https://fonts.googleapis.com/css2?family=Poppins:wght@600;700&family=Oswald:wght@500&display=swap" rel="stylesheet">
<style>
  :root {
    --sky-top: #2a55b8;
    --sky-bottom: #6f94d8;
    --band: rgba(46, 138, 232, 0.88);
    --title-yellow: #ffff1a;
    --white: #ffffff;
    --mortar: #8d918c;
    --brick: #b2603f;
    --brick-edge: #8f4a30;
    --ground: #6b706f;
  }
  html, body {
    margin: 0;
    padding: 0;
    overflow: hidden;
    background: var(--white);
  }
  .postcard {
    position: relative;
    width: 857px;
    height: 1200px;
    overflow: hidden;
    background: linear-gradient(180deg, var(--sky-top) 0%, var(--sky-bottom) 52%);
  }
  .sky-photo, .child-photo, .toys-photo {
    position: absolute;
  }
  .sky-photo {
    left: 0; top: 0; width: 857px; height: 620px;
    background: radial-gradient(ellipse at 10% 20%, rgba(255,255,255,0.35), rgba(255,255,255,0) 45%);
  }
  .child-photo {
    left: 200px; top: 30px; width: 440px; height: 595px;
    background: linear-gradient(180deg, rgba(240,230,220,0.22), rgba(200,180,160,0.18));
    border-radius: 40px;
  }
  .accent-line {
    position: absolute;
    height: 9px;
  }
  .accent-line--yellow { left: 0; top: 219px; width: 268px; background: var(--title-yellow); }
  .accent-line--white { left: 553px; top: 410px; width: 304px; background: var(--white); }
  .title-band {
    position: absolute;
    left: 0; top: 240px; width: 857px; height: 158px;
    background: var(--band);
    text-align: center;
    font-family: 'Poppins', sans-serif;
  }
  .title {
    margin: 0;
    padding-top: 19px;
    font-weight: 700;
    font-size: 57px;
    line-height: 68px;
    color: var(--white);
    letter-spacing: -0.5px;
  }
  .title .highlight { color: var(--title-yellow); }
  .subtitle {
    margin: 6px 0 0;
    font-weight: 600;
    font-size: 29px;
    line-height: 36px;
    color: var(--white);
  }
  .wall {
    position: absolute;
    left: 0; top: 620px; width: 857px; height: 286px;
    background: var(--mortar);
  }
  .brick {
    position: absolute;
    display: flex;
    align-items: center;
    justify-content: center;
    text-align: center;
    background: var(--brick);
    box-shadow: inset 0 -3px 0 var(--brick-edge), inset 0 2px 0 rgba(255,255,255,0.08);
    font-family: 'Oswald', sans-serif;
    font-weight: 500;
    font-size: 25px;
    line-height: 25px;
    color: var(--white);
    text-shadow: 1px 1px 2px rgba(0,0,0,0.45);
  }
  .brick--two-line { font-size: 23px; line-height: 25px; }
  .row-1 { top: 6px; height: 57px; }
  .row-2 { top: 80px; height: 57px; }
  .row-3 { top: 151px; height: 58px; }
  .row-4 { top: 223px; height: 60px; }
  .ground {
    position: absolute;
    left: 0; top: 906px; width: 857px; height: 294px;
    background: var(--ground);
  }
  .toys-photo {
    left: 0; top: 20px; width: 857px; height: 274px;
    background: linear-gradient(90deg, rgba(160,60,160,0.35), rgba(230,200,40,0.3) 45%, rgba(230,140,80,0.3) 80%, rgba(100,90,80,0.2));
  }
</style>
</head>
<body>
<div class="postcard">
  <div class="sky-photo" role="img" aria-label="Blue sky with soft white clouds"></div>
  <div class="child-photo" role="img" aria-label="Smiling young boy in a white t-shirt and denim shorts standing on the wall with arms raised, holding a colourful puzzle cube"></div>

  <div class="accent-line accent-line--yellow"></div>
  <header class="title-band">
    <h1 class="title"><span class="highlight">Speech/Language</span> Therapy</h1>
    <p class="subtitle">The Foundation for Communication Success</p>
  </header>
  <div class="accent-line accent-line--white"></div>

  <section class="wall" aria-label="Areas of therapy">
    <div class="brick row-1" style="left:0;width:80px"></div>
    <div class="brick row-1" style="left:97px;width:258px">Receptive Language</div>
    <div class="brick row-1" style="left:375px;width:256px">Expressive Language</div>
    <div class="brick row-1" style="left:650px;width:207px">Social Language</div>

    <div class="brick row-2" style="left:0;width:14px"></div>
    <div class="brick row-2" style="left:30px;width:124px">Sensory</div>
    <div class="brick row-2" style="left:169px;width:125px">Cognitive</div>
    <div class="brick row-2" style="left:313px;width:124px">Pragmatics</div>
    <div class="brick row-2" style="left:453px;width:122px">Autism</div>
    <div class="brick row-2" style="left:593px;width:124px">Articulation</div>
    <div class="brick row-2" style="left:731px;width:117px">Goals</div>

    <div class="brick row-3" style="left:0;width:79px">ASD</div>
    <div class="brick row-3 brick--two-line" style="left:95px;width:260px">Environmental<br>Communication</div>
    <div class="brick row-3" style="left:374px;width:256px">Auditory Processing</div>
    <div class="brick row-3" style="left:650px;width:207px">Mirror Neurons</div>

    <div class="brick row-4" style="left:0;width:7px"></div>
    <div class="brick row-4" style="left:22px;width:128px">TeleTherapy</div>
    <div class="brick row-4" style="left:165px;width:122px">Evaluation</div>
    <div class="brick row-4" style="left:306px;width:122px">Screening</div>
    <div class="brick row-4 brick--two-line" style="left:443px;width:123px">Family<br>Involvement</div>
    <div class="brick row-4" style="left:582px;width:269px">Developmental Delay</div>
  </section>

  <div class="ground">
    <div class="toys-photo" role="img" aria-label="Colourful puzzle pieces, wooden building blocks and a partly assembled picture puzzle on a grey floor"></div>
  </div>
</div>
</body>
</html>
```